Burlesque theatre show about a future American dystopia needs poster design

I am looking for a highly creative and arresting design for a promotional poster for a production of my play, Tin Lantern Waltz. Here is a little bit about the project:

Tin Lantern Waltz is a new Canadian play about love blossoming in the hardest of times. Set 100 years from now in a dystopian American landscape of drugs, sex, and rock n' roll, one girl dares to dream of a better world far away in the icy Canadian arctic. The last refuge of artists and philosophers in a world controlled by despotic corporations, this final frontier of untouched beauty becomes the only beacon of hope for Mira, who finds her innocence increasingly threatened by the power-hungry and fame obsessed adults in her life. A chronicle of finding hope even in the darkest of times, Tin Lantern Waltz intertwines burlesque and opera with a powerful story of violence, love, and redemption to create a visceral in-your-face theatre experience.

Some imagery from the play: guns, feather boas, Mexican day of the dead, burlesque, roses....

Target Market(s)

Ages 18-65, people in Vancouver, people who like live theatre, opera, burlesque, new plays.

Industry/Entity Type

Promotional

Font styles to use
Other font styles liked:
• Old Press by Renzo Falkrid, Capture It by Vörösmart GéZa, Tiza by Tomas Feliu, TOSCA ZERO by Denny Strauk, Very Damaged Bold by Renzo Falkrid, MAJOR GUILTY by Denny Strauk

Colors
ec1f27
f04a51
0255a3
0792cd
33a6d7
00a990
33b8a4
9bcb3c

Requirements
Must have
• Important info about dates, time, and location on the poster.
Nice to have
• I'm looking for something sexy but not vulgar in any way. This play is urban and gritty, and perhaps the font should reflect that.

```html
<!DOCTYPE html>
<html lang="en">
<head>
<meta charset="utf-8">
<title>Tin Lantern Waltz — Poster</title>
<link rel="stylesheet" href="https://fonts.googleapis.com/css2?family=Bebas+Neue&family=Special+Elite&display=swap">
<style>
  :root {
    --ink-night: #0d0707;
    --ink-ember: #3a1512;
    --rose-red: #ec1f27;
    --rose-soft: #f04a51;
    --blue-deep: #0255a3;
    --blue-mid: #0792cd;
    --sky-blue: #33a6d7;
    --teal-deep: #00a990;
    --teal-soft: #33b8a4;
    --leaf-green: #9bcb3c;
    --skin-pale: #e9ddd6;
    --paper: #f4efe6;
    --paper-dim: #e6ddd0;
  }
  * { margin: 0; padding: 0; box-sizing: border-box; }
  html, body { width: 849px; height: 1200px; overflow: hidden; background: var(--ink-night); }
  .poster {
    position: relative;
    width: 849px;
    height: 1200px;
    overflow: hidden;
    background: radial-gradient(ellipse at 50% 45%, #3d1512 0%, #1e0c0a 60%, #0a0505 100%);
    color: var(--paper);
  }
  .poster::after {
    content: "";
    position: absolute;
    inset: 0;
    box-shadow: inset 0 0 120px 30px rgba(0,0,0,0.8);
    pointer-events: none;
  }
  .hero-art {
    position: absolute;
    left: 0;
    top: 0;
    width: 849px;
    height: 900px;
    background:
      radial-gradient(ellipse 150px 190px at 50% 34%, var(--skin-pale) 0%, #d9b4a8 45%, rgba(190,70,60,0.9) 85%, rgba(190,70,60,0) 100%),
      radial-gradient(ellipse 230px 150px at 56% 72%, rgba(236,31,39,0.95) 0%, rgba(170,35,30,0.85) 50%, rgba(120,25,20,0) 100%),
      radial-gradient(ellipse 200px 260px at 50% 45%, rgba(40,18,16,0.95) 0%, rgba(40,18,16,0.6) 70%, rgba(40,18,16,0) 100%),
      radial-gradient(circle at 21% 10%, rgba(130,90,160,0.85) 0 55px, rgba(130,90,160,0) 95px),
      radial-gradient(circle at 34% 7%, rgba(0,169,144,0.8) 0 45px, rgba(0,169,144,0) 80px),
      radial-gradient(circle at 12% 33%, rgba(7,146,205,0.85) 0 60px, rgba(7,146,205,0) 100px),
      radial-gradient(circle at 14% 52%, rgba(155,203,60,0.9) 0 55px, rgba(155,203,60,0) 95px),
      radial-gradient(circle at 26% 58%, rgba(51,184,164,0.7) 0 40px, rgba(51,184,164,0) 75px),
      radial-gradient(circle at 86% 18%, rgba(130,90,160,0.8) 0 70px, rgba(130,90,160,0) 115px),
      radial-gradient(circle at 74% 30%, rgba(155,203,60,0.9) 0 55px, rgba(155,203,60,0) 95px),
      radial-gradient(circle at 84% 43%, rgba(51,166,215,0.9) 0 60px, rgba(51,166,215,0) 100px),
      radial-gradient(circle at 88% 28%, rgba(240,74,81,0.7) 0 40px, rgba(240,74,81,0) 75px),
      linear-gradient(90deg, rgba(60,40,40,0.9) 0%, rgba(60,40,40,0) 30%),
      linear-gradient(180deg, #2a1411 0%, #3a1613 55%, #1e0c0a 85%, rgba(13,7,7,0) 100%);
  }
  .tagline {
    position: absolute;
    top: 24px;
    left: 0;
    width: 100%;
    text-align: center;
    font-family: "Special Elite", monospace;
    font-size: 27px;
    line-height: 1.1;
    letter-spacing: 1px;
    color: var(--paper-dim);
    text-transform: uppercase;
    text-shadow: 0 2px 6px rgba(0,0,0,0.7);
  }
  .title {
    position: absolute;
    top: 718px;
    left: 0;
    width: 100%;
    text-align: center;
    font-family: "Bebas Neue", sans-serif;
    font-weight: 400;
    color: var(--paper);
    text-transform: uppercase;
    line-height: 0.8;
    text-shadow: 0 3px 10px rgba(0,0,0,0.7);
  }
  .title-line { display: block; }
  .title-line--top { font-size: 146px; letter-spacing: 6px; }
  .title-line--bottom { font-size: 158px; letter-spacing: 40px; margin-left: 40px; }
  .details {
    position: absolute;
    top: 988px;
    left: 0;
    width: 100%;
    text-align: center;
    font-family: "Special Elite", monospace;
    text-transform: uppercase;
    color: var(--paper-dim);
  }
  .subtitle { font-size: 17px; letter-spacing: 2px; margin-bottom: 10px; }
  .schedule { font-size: 24px; letter-spacing: 1px; line-height: 1.15; }
  .venue { font-size: 24px; letter-spacing: 1px; margin-top: 6px; }
  .website { margin-top: 14px; font-size: 22px; letter-spacing: 3px; }
</style>
</head>
<body>
  <main class="poster">
    <div class="hero-art" role="img" aria-label="Photograph of a woman in Day of the Dead sugar skull makeup in a red dress, surrounded by blue, green and purple flowers over a dim ruined city"></div>

    <p class="tagline">In the ruins of America<br>one girl dreams of a better life.</p>

    <h1 class="title">
      <span class="title-line title-line--top">Tin Lantern</span>
      <span class="title-line title-line--bottom">Waltz</span>
    </h1>

    <section class="details">
      <p class="subtitle">A burlesque tragicomedy of love and redemption</p>
      <p class="schedule">June 2 - 8 @ 7:30 PM<br>Sat-Sun 2:00 PM and 7:30 PM</p>
      <p class="venue">The Forge Theatre 48 North 7th Ave, $15</p>
      <p class="website">http://www.theatre-kestrel.com</p>
    </section>
  </main>
</body>
</html>
```